Alarm System package Ad for Facebook and flyer

Looking to create a Facebook add & flyer (A4) for an alarm system package
It will be used in paid Facebook advertising and letterbox drops
Once design is decided I will require 2-3 different pricing versions but using the same layout/design

The alarm package is a very cheap deal and the system itself if most suitable for smaller homes and smaller businesses.
The package includes back to base alarm monitoring on a contract for a minimum 12 months. This is at an additional cost (terms and conditions will explain this)

Target Market(s)

families, small business owners, home owners,

Industry/Entity Type

Advertising

Font styles to use
Sans Serif

Colors

Designer to choose colors to be used in the design.

Requirements
Must have
• Harbourline Guard logo to be easily visible
• the alarm package will be priced at $299 (and 2 other version will be required upon approval of design)
• it will need a section to state terms and conditions apply
• QLT Ready (logo)
• Image of the parts
• minimal wording eg'Fully installed monitored alarm system" then the price
Nice to have
• family and/or home in the background
• Colors similar to my logo
• Logo on the ad
Should not have
• must not have a corporate feel

```html
<!DOCTYPE html>
<html lang="en">
<head>
<meta charset="utf-8">
<title>Harbourline Guard – Alarm Package Flyer</title>
<link href="https://fonts.googleapis.com/css2?family=Oswald:wght@500;700&family=Roboto+Condensed:wght@300;400;700&display=swap" rel="stylesheet">
<style>
  :root {
    --frame: #58585a;
    --paper: #ffffff;
    --navy: #1f3368;
    --blue: #1e9bd7;
    --sky: #2aa7e0;
    --ink: #1a1a1a;
    --photo-top: #4a4038;
    --photo-mid: #6d7f5a;
    --photo-low: #4f8a2e;
    --device: #dfe1e4;
  }
  * { box-sizing: border-box; margin: 0; padding: 0; }
  html, body { width: 868px; height: 1200px; overflow: hidden; background: var(--frame); }
  .canvas { position: relative; width: 868px; height: 1200px; background: var(--frame); }
  .flyer {
    position: absolute; left: 51px; top: 58px; width: 766px; height: 1082px;
    background: var(--paper); overflow: hidden;
    font-family: "Roboto Condensed", Arial, sans-serif; color: var(--ink);
  }
  .hero-art { position: absolute; left: 0; top: 0; width: 766px; height: 720px; }
  .intro {
    position: absolute; left: 23px; top: 599px;
    font-size: 15.5px; font-weight: 300; line-height: 20.4px; white-space: nowrap;
  }
  .headline {
    position: absolute; left: 23px; top: 680px;
    font-family: "Oswald", "Arial Narrow", sans-serif; font-weight: 500;
    font-size: 38px; line-height: 40px; color: var(--blue); letter-spacing: -0.5px;
    white-space: nowrap;
    transform: scaleX(0.86); transform-origin: left;
  }
  .price {
    position: absolute; left: 16px; top: 698px; z-index: 1;
    font-family: "Oswald", "Arial Narrow", sans-serif; font-weight: 700;
    color: var(--navy); font-size: 248px; line-height: 248px; letter-spacing: -5px;
    white-space: nowrap;
    transform: scaleX(1.075); transform-origin: left top;
  }
  .price-currency {
    position: absolute; left: 29px; top: 800px; z-index: 2;
    font-family: "Oswald", sans-serif; font-weight: 700; font-size: 46px; line-height: 54px; color: #000;
  }
  .parts {
    position: absolute; left: 435px; top: 649px; width: 308px; height: 243px;
    border-radius: 10px;
    background: radial-gradient(ellipse at 55% 45%, var(--device) 0%, #eef0f2 55%, var(--paper) 80%);
  }
  .terms {
    position: absolute; left: 437px; top: 897px;
    font-size: 10.5px; line-height: 13.9px; font-weight: 400; white-space: nowrap;
  }
  .rule { position: absolute; left: 0; top: 944px; width: 766px; height: 3px; background: var(--navy); }
  .partner-bar { position: absolute; left: 0; top: 950px; width: 766px; height: 132px; }
  .qlt {
    position: absolute; left: 86px; top: 30px; display: flex; align-items: center; gap: 14px;
    font-family: "Roboto Condensed", sans-serif; font-weight: 400; font-size: 46px; line-height: 70px; color: var(--navy);
  }
  .qlt-dot { width: 58px; height: 58px; border-radius: 50%; background: var(--blue); }
  .ready-badge { position: absolute; left: 283px; top: 38px; width: 134px; height: 46px; background: var(--sky); }
  .divider { position: absolute; left: 432px; top: 28px; width: 2px; height: 74px; background: #c9ccd3; }
  .brand {
    position: absolute; left: 450px; top: 36px; display: flex; align-items: center; gap: 12px;
  }
  .brand-mark { width: 48px; height: 48px; background: var(--navy); }
  .brand-name {
    font-family: "Roboto Condensed", sans-serif; font-weight: 700; font-size: 26px;
    line-height: 28px; color: var(--navy); text-transform: uppercase; width: 190px;
  }
</style>
</head>
<body>
<div class="canvas">
  <main class="flyer">
    <svg class="hero-art" viewBox="0 0 766 720">
      <defs>
        <linearGradient id="swoosh-light" x1="0" y1="0" x2="0" y2="1">
          <stop offset="0" stop-color="#2aa7e0"/>
          <stop offset="1" stop-color="#1b6fb4"/>
        </linearGradient>
        <linearGradient id="photo-tone" x1="0" y1="0" x2="0" y2="1">
          <stop offset="0" stop-color="#4a4038"/>
          <stop offset="0.55" stop-color="#6d7f5a"/>
          <stop offset="1" stop-color="#4f8a2e"/>
        </linearGradient>
      </defs>
      <circle class="swoosh-navy" cx="500" cy="198" r="445" fill="#1f3368"/>
      <circle class="swoosh-blue" cx="518" cy="212" r="418" fill="url(#swoosh-light)"/>
      <circle class="swoosh-white" cx="532" cy="220" r="390" fill="#ffffff"/>
      <circle class="family-photo" cx="540" cy="226" r="375" fill="url(#photo-tone)"
              role="img" aria-label="Photo of a smiling family swinging their young daughter on the front lawn of their home"/>
    </svg>

    <p class="intro">The alarm package is a very<br>cheap deal and the system itself<br>if most suitable for smaller homes<br>and smaller businesses.</p>
    <h1 class="headline">SECURE YOUR HOME</h1>
    <div class="price">299</div>
    <div class="price-currency">$</div>

    <div class="parts" role="img" aria-label="Alarm system parts: keypad control panel, two motion sensors, door contact and key fob remote"></div>
    <p class="terms">The package includes back to base alarm monitoring on a contract<br>for a minimum 12 months. This is at an additional cost (terms and<br>conditions will explain this)</p>

    <div class="rule"></div>
    <footer class="partner-bar">
      <div class="qlt"><span>QLT</span><span class="qlt-dot"></span></div>
      <div class="ready-badge"></div>
      <div class="divider"></div>
      <div class="brand">
        <span class="brand-mark"></span>
        <span class="brand-name">Harbourline Guard</span>
      </div>
    </footer>
  </main>
</div>
</body>
</html>
```